Your complete Gardening and lawn maintenance, Horticultural care. (to be on card)
We are looking at using a logo of a tree, with a recycling emblem circling the tree. The colors of choice, are burnt oranges and olive greens. Presented; simple to the eye, yet catchy to the clients in a eco-friendly way. We have uploaded a design for you to look at just to give a rough idea, you can use that or create your own ideas or play around with a mixture.

Target Market(s)

Home owners, businesses, real estates.

Industry/Entity Type

Recycling

Contact Information for Business Card

Name: Derek Ostrowe
Phone: 0421583906
Email: bramblewoodyards@mailnest.net

Logo Text

Bramble-Wood Yards

Logo styles of interest
Emblem Logo
Pictorial/Combination Logo
Abstract Logo
Requirements
Must have
• Business name: Bramble-Wood Yards
and slogan : Your complete Gardening and lawn maintenance, Horticultural care

```html
<!DOCTYPE html>
<html lang="en">
<head>
<meta charset="utf-8">
<title>Bramble-Wood Yards — Business Card</title>
<link rel="stylesheet" href="https://fonts.googleapis.com/css2?family=Cormorant+Garamond:ital,wght@0,500;1,600&family=Tinos&display=swap">
<style>
  :root {
    --card-stone: #dcdde2;
    --card-stone-light: #e9eaee;
    --accent-crimson: #931a1e;
    --brand-green: #1f8a3d;
    --mark-olive: #7b7a36;
    --ink-cream: #f4ecdc;
    --icon-green: #2f8a45;
    --icon-blue: #2f6fb8;
  }
  html, body {
    margin: 0;
    padding: 0;
    width: 1200px;
    height: 695px;
    overflow: hidden;
    background: #ffffff;
  }
  .card {
    position: relative;
    width: 1200px;
    height: 695px;
    overflow: hidden;
    background: radial-gradient(ellipse at 35% 40%, var(--card-stone-light), var(--card-stone) 75%);
    font-family: "Cormorant Garamond", Georgia, serif;
  }
  .card__panel {
    position: absolute;
    inset: 0;
    width: 1200px;
    height: 695px;
  }
  .brand-mark {
    position: absolute;
    left: 156px;
    top: 45px;
    width: 258px;
    height: 258px;
    border-radius: 50%;
    background: var(--mark-olive);
  }
  .brand {
    position: absolute;
    left: 26px;
    top: 404px;
    width: 500px;
  }
  .brand__name {
    margin: 0;
    font-family: "Cormorant Garamond", Georgia, serif;
    font-style: italic;
    font-weight: 600;
    font-size: 62px;
    line-height: 1;
    color: var(--brand-green);
    white-space: nowrap;
  }
  .brand__slogan {
    margin: 14px 0 0 4px;
    max-width: 470px;
    font-family: "Cormorant Garamond", Georgia, serif;
    font-style: italic;
    font-weight: 600;
    font-size: 21px;
    line-height: 1.25;
    color: var(--brand-green);
  }
  .contact {
    position: absolute;
    left: 760px;
    top: 408px;
    color: var(--ink-cream);
  }
  .contact__name {
    margin: 0 0 22px 72px;
    font-family: "Cormorant Garamond", Georgia, serif;
    font-style: italic;
    font-weight: 600;
    font-size: 56px;
    line-height: 1;
    white-space: nowrap;
    text-shadow: 1px 2px 3px rgba(0, 0, 0, 0.45);
  }
  .contact__row {
    display: flex;
    align-items: center;
    height: 48px;
    margin-bottom: 4px;
  }
  .contact__icon {
    width: 44px;
    height: 32px;
    flex: none;
  }
  .contact__phone {
    margin-left: 34px;
    font-family: "Tinos", "Times New Roman", serif;
    font-size: 27px;
    letter-spacing: 3px;
  }
  .contact__email {
    margin-left: 17px;
    font-family: "Tinos", "Times New Roman", serif;
    font-size: 24.5px;
    white-space: nowrap;
  }
</style>
</head>
<body>
<main class="card">
  <svg class="card__panel" viewBox="0 0 1200 695" aria-hidden="true">
    <defs>
      <filter id="panel-shadow" x="-20%" y="-10%" width="140%" height="120%">
        <feDropShadow dx="-6" dy="4" stdDeviation="8" flood-color="#000" flood-opacity="0.35"/>
      </filter>
    </defs>
    <path filter="url(#panel-shadow)" fill="var(--accent-crimson)"
      d="M1060,0 L1200,0 L1200,695 L745,695 C702,640 688,560 718,470 C775,310 950,140 1060,0 Z"/>
  </svg>

  <div class="brand-mark" aria-hidden="true"></div>
  <header class="brand">
    <h1 class="brand__name">Bramble-Wood Yards</h1>
    <p class="brand__slogan">Your complete Gardening and lawn maintenance, Horticultural care</p>
  </header>

  <section class="contact">
    <p class="contact__name">Derek Ostrowe</p>
    <div class="contact__row">
      <svg class="contact__icon" viewBox="0 0 44 32" aria-hidden="true">
        <ellipse cx="22" cy="16" rx="21" ry="15" fill="var(--icon-green)"/>
        <path d="M11 13 C11 8 33 8 33 13 L29 14 L28 11 L16 11 L15 14 Z" fill="#fff"/>
        <rect x="14" y="15" width="16" height="9" rx="2" fill="#fff"/>
        <circle cx="22" cy="19.5" r="2.2" fill="var(--icon-green)"/>
      </svg>
      <span class="contact__phone">0421583906</span>
    </div>
    <div class="contact__row">
      <svg class="contact__icon" viewBox="0 0 44 32" aria-hidden="true">
        <rect x="4" y="5" width="34" height="23" rx="2" fill="#fff" stroke="var(--icon-blue)" stroke-width="2"/>
        <path d="M5 6 L21 19 L37 6" fill="none" stroke="var(--icon-blue)" stroke-width="2"/>
        <circle cx="21" cy="13" r="5" fill="none" stroke="var(--icon-blue)" stroke-width="1.6"/>
      </svg>
      <span class="contact__email">bramblewoodyards@mailnest.net</span>
    </div>
  </section>
</main>
</body>
</html>
```